Website Design for Freeze-Dried Food Manufacturing Company (Pet Food & Agri-Food)

We are looking for a high-level web designer to create a clean, modern, premium website design for Tarquel, a freeze-dried food manufacturing company operating in both the pet food and agri-food space.
This is not a basic website build β we are looking for a designer who understands brand positioning, layout, and user flow, not just visuals.
π― Project Objective
Design a website that:
Clearly communicates our capabilities and value proposition
Feels premium, credible, and product-driven
Guides users through a simple, intuitive journey
Clean and Crips
A critical requirement is clearly separating:
π Pet Food
π Agri-Food
These must feel like two distinct pathways within the same brand experience.
We have attached detailed documents outlining structure, layout, and messaging. These should be followed closely.
π What Success Looks Like
A high-impact homepage with strong visual hierarchy
Clear entry points into Pet Food and Agri-Food
Clean, intentional layout (not cluttered or template-like)
Thoughtful spacing, typography, and flow
A design that feels considered and elevated, not generic
π¨ Design Direction
We are aiming for a:
Minimal, premium aesthetic
Warm, natural color palette (creams, browns, muted tones)
Ingredient and product-focused visuals
Avoid:
Overly corporate / industrial styles
Generic SaaS-style layouts
Busy or over-designed interfaces
End Goal
A website that immediately communicates:
Who we are
What we do
Why weβre different
In a way that feels premium, clear, and easy to navigate.
Link to current website: https://tarquelfoods.example/
https://tarquelhealth.example/wp-admin/

```html
<!DOCTYPE html>
<html lang="en">
<head>
<meta charset="utf-8">
<title>Tarquel – Pet Food Applications</title>
<link href="https://fonts.googleapis.com/css2?family=Playfair+Display:wght@400;500&family=Poppins:wght@400;500;600&display=swap" rel="stylesheet">
<style>
:root{
  --cream:#f8f3ec;
  --cream-2:#f2eae0;
  --band-1:#f1e8de;
  --band-2:#e9dfd3;
  --band-3:#e2d8cb;
  --copper:#b97650;
  --copper-light:#d08a5c;
  --copper-dark:#9a5c3a;
  --ink:#2f2219;
  --text:#3d3029;
  --muted:#6b5c52;
  --line:#d9b79d;
}
*{box-sizing:border-box;margin:0;padding:0}
html,body{width:1200px;height:4107px;overflow:hidden}
body{background:var(--cream);font-family:'Poppins',sans-serif;color:var(--text);position:relative}
.abs{position:absolute}
.serif{font-family:'Playfair Display',serif}

/* header */
.logo{font-family:'Poppins',sans-serif;font-weight:400;color:var(--copper);font-size:44px;letter-spacing:1px;line-height:1}
.site-header .logo{left:110px;top:36px}
.main-nav{left:338px;top:56px;display:flex;gap:28px;font-size:13px;font-weight:500;color:var(--ink)}
.main-nav .active{color:var(--copper-light);text-decoration:underline;text-underline-offset:5px}
.btn{display:inline-flex;align-items:center;justify-content:center;border-radius:30px;font-weight:600;letter-spacing:.5px;text-transform:uppercase}
.btn-contact{left:957px;top:41px;width:132px;height:48px;background:var(--copper);color:#fff;font-size:15px}

/* hero */
.hero-art{left:0;top:0}
.hero-rule{left:111px;top:192px;width:3px;height:342px;background:var(--ink)}
.eyebrow{left:146px;top:232px;font-size:18px;color:var(--copper-light);display:flex;align-items:center;gap:20px}
.eyebrow::after{content:"";width:224px;height:1px;background:var(--line)}
.hero-title{left:146px;top:258px;font-size:52px;color:var(--ink);font-weight:400}
.hero-text{left:148px;top:330px;width:440px;font-size:19.5px;line-height:31px;font-weight:500;color:var(--text)}
.btn-hero{left:148px;top:443px;width:186px;height:46px;background:var(--copper);color:#fff;font-size:14.5px}

/* section titles */
.section-title{left:0;width:1200px;text-align:center;font-family:'Playfair Display',serif;font-size:46px;color:var(--ink);font-weight:400;line-height:1.1}
.section-title::after{content:"";display:block;width:90px;height:2px;background:var(--copper-light);margin:16px auto 0}

/* categories */
.cat-photo{width:427px;height:281px;border-radius:7px;box-shadow:0 12px 26px rgba(90,60,40,.18)}
.cat-label{width:427px;text-align:center;font-size:20px;font-weight:500;color:var(--ink);line-height:31px;text-transform:uppercase}

/* services band */
.service{top:1618px;width:400px;height:300px;text-align:center;padding-top:48px}
.service svg{display:block;margin:0 auto}
.service h3{margin-top:16px;font-size:20px;font-weight:600;color:var(--ink)}
.service p{margin:10px auto 0;width:320px;font-size:17.5px;line-height:29px;color:var(--muted)}

/* process */
.process-bg{left:0;top:1918px;width:1200px;height:640px;background:linear-gradient(180deg,var(--cream) 0%,var(--cream-2) 60%,#eee4d8 100%)}
.step-label{width:200px;text-align:center;font-size:18px;font-weight:600;color:var(--ink)}

/* storage */
.lead{left:0;width:1200px;text-align:center;font-size:19px;line-height:30px;color:var(--text);font-weight:500}
.store-card{top:2864px;width:303px;height:375px;background:#f8f1e9;border-radius:16px;box-shadow:0 8px 28px rgba(110,80,55,.12);text-align:center;padding-top:46px}
.store-card svg{display:block;margin:0 auto}
.store-card h3{margin-top:20px;font-size:19px;font-weight:600;line-height:29px;color:var(--ink);text-transform:uppercase}
.store-card .dot{width:7px;height:7px;border-radius:50%;background:var(--copper-light);margin:10px auto 0}
.store-card p{margin:14px auto 0;width:250px;font-size:17px;line-height:29px;color:var(--muted)}

/* cta */
.cta{left:0;top:3461px;width:1200px;height:430px;background:linear-gradient(180deg,#b97a53 0%,#c3865c 55%,#cf9165 100%)}
.cta-title{left:0;top:3530px;width:1200px;text-align:center;font-family:'Playfair Display',serif;font-size:48px;line-height:57px;color:#fbf3ea}
.cta-text{left:0;top:3672px;width:1200px;text-align:center;font-size:19px;line-height:30px;color:#fbf1e6}
.btn-cta{left:507px;top:3757px;width:187px;height:46px;background:#fbf6f0;color:var(--ink);font-size:14.5px}

/* footer */
.site-footer .logo{left:110px;top:3952px}
.foot-nav{left:365px;top:3967px;display:flex;gap:29px;font-size:14px;font-weight:500;color:var(--ink)}
.foot-rule{left:110px;top:4022px;width:980px;height:1px;background:#e4d5c6}
.copyright{left:0;top:4045px;width:1200px;text-align:center;font-size:12px;color:var(--muted)}
.social{top:4036px;width:36px;height:36px;border-radius:50%;background:#f1e8de}
.social.primary{background:var(--copper)}
</style>
</head>
<body>

<header class="site-header">
  <div class="abs logo">Tarquel</div>
  <nav class="abs main-nav">
    <span>Home</span><span>About</span><span class="active">Applications</span><span>Capabilities</span><span>Quality &amp; Traceability</span><span>Why Tarquel</span>
  </nav>
  <a class="abs btn btn-contact">Contact</a>
</header>

<section class="hero">
  <svg class="abs hero-art" width="1200" height="600" viewBox="0 0 1200 600" role="img" aria-label="Golden retriever and tabby cat sitting by a bowl of freeze-dried pet food in a bright kitchen">
    <defs>
      <linearGradient id="heroGrad" x1="0" y1="0" x2="1" y2="1">
        <stop offset="0" stop-color="#efe3d4"/>
        <stop offset=".45" stop-color="#c9965f"/>
        <stop offset=".75" stop-color="#a87650"/>
        <stop offset="1" stop-color="#d8c8b6"/>
      </linearGradient>
    </defs>
    <polygon points="1000,0 1200,0 1200,590 872,590 702,375" fill="url(#heroGrad)"/>
  </svg>
  <div class="abs hero-rule"></div>
  <div class="abs eyebrow">APPLICATIONS</div>
  <h1 class="abs hero-title serif">Pet Food</h1>
  <p class="abs hero-text">We develop premium freeze-dried pet food products designed for performance, palatability, and consistency.</p>
  <a class="abs btn btn-hero">Start a Project</a>
</section>

<section class="categories">
  <h2 class="abs section-title" style="top:676px">CATEGORIES</h2>
  <div class="abs cat-photo" style="left:155px;top:784px;background:linear-gradient(135deg,#8a5a36,#c9a37a 50%,#7a4c2e)" role="img" aria-label="Bags of dog food with bowls of kibble on a wooden table"></div>
  <div class="abs cat-label" style="left:155px;top:1088px">K9 Veterinary Certified<br>Complete &amp; Balanced Meals</div>
  <div class="abs cat-photo" style="left:617px;top:784px;background:linear-gradient(135deg,#5d4a3d,#a8825c 55%,#3f2d22)" role="img" aria-label="Scoop of freeze-dried pucks with a small dog in the background"></div>
  <div class="abs cat-label" style="left:617px;top:1088px">Pucks and Cubes</div>
  <div class="abs cat-photo" style="left:155px;top:1181px;background:linear-gradient(135deg,#3a2b22,#6b7a62 45%,#3e6670 75%,#2a2520)" role="img" aria-label="Pet food pouches lined up on a warmly lit shelf"></div>
  <div class="abs cat-label" style="left:155px;top:1483px">Powders and Toppers</div>
  <div class="abs cat-photo" style="left:617px;top:1181px;background:linear-gradient(135deg,#c9b9a4,#8c7a68 50%,#d9c9b3)" role="img" aria-label="Person pouring pet food from a large bag into a storage container in a kitchen"></div>
  <div class="abs cat-label" style="left:617px;top:1483px">Custom Formats</div>
</section>

<section class="services">
  <div class="abs service" style="left:0;background:var(--band-1)">
    <svg width="66" height="66" viewBox="0 0 66 66" fill="none" stroke="#c47c4f" stroke-width="2">
      <circle cx="33" cy="33" r="26"/><circle cx="33" cy="33" r="18"/>
      <path d="M33 22l10 5v12l-10 5-10-5V27z M23 27l10 5 10-5 M33 32v12"/>
    </svg>
    <h3>OEM / PRIVATE LABEL</h3>
    <p>Custom product development from concept to commercialization</p>
  </div>
  <div class="abs service" style="left:400px;background:var(--band-2)">
    <svg width="66" height="66" viewBox="0 0 66 66" fill="none" stroke="#c47c4f" stroke-width="2">
      <path d="M8 26L33 10l25 16v32H8z"/><rect x="16" y="30" width="26" height="22"/><path d="M29 34v14M22 41h14M24 36l10 10M34 36L24 46"/><rect x="47" y="30" width="5" height="22" rx="2"/>
    </svg>
    <h3>FREEZE DRYING</h3>
    <p>Industrial freeze-drying for food, ingredients, and agricultural products</p>
  </div>
  <div class="abs service" style="left:800px;background:var(--band-3)">
    <svg width="66" height="66" viewBox="0 0 66 66" fill="none" stroke="#c47c4f" stroke-width="2">
      <circle cx="33" cy="30" r="14"/><circle cx="33" cy="30" r="6"/><path d="M27 44v8h12v-8M29 56h8M33 6v6M15 12l4 4M51 12l-4 4M9 30h6M51 30h6"/>
    </svg>
    <h3>R&amp;D TEST KITCHEN</h3>
    <p>Pilot runs, formulation, and product optimization</p>
  </div>
</section>

<section class="process">
  <div class="abs process-bg"></div>
  <h2 class="abs section-title" style="top:2018px">OUR PROCESS</h2>
  <div class="abs step-label" style="left:118px;top:2126px">DISCOVERY</div>
  <div class="abs step-label" style="left:424px;top:2126px">R&amp;D</div>
  <div class="abs step-label" style="left:730px;top:2126px">PRODUCTION</div>
  <div class="abs step-label" style="left:271px;top:2443px">SOURCING</div>
  <div class="abs step-label" style="left:577px;top:2443px">PILOT</div>
  <div class="abs step-label" style="left:883px;top:2443px">PACKAGING</div>
  <svg class="abs" style="left:0;top:2140px" width="1200" height="320" viewBox="0 2140 1200 320" fill="none">
    <defs>
      <linearGradient id="wave" x1="0" y1="0" x2="1" y2="0">
        <stop offset="0" stop-color="#a8673f"/><stop offset="1" stop-color="#c98c60"/>
      </linearGradient>
      <filter id="soft" x="-20%" y="-20%" width="140%" height="140%"><feDropShadow dx="0" dy="4" stdDeviation="5" flood-color="#8a5a3a" flood-opacity=".18"/></filter>
    </defs>
    <g stroke="#b97650" stroke-width="2">
      <path d="M218 2168v55M524 2168v55M830 2168v55M371 2377v52M677 2377v52M983 2377v52"/>
    </g>
    <g fill="#b97650">
      <circle cx="218" cy="2168" r="5"/><circle cx="524" cy="2168" r="5"/><circle cx="830" cy="2168" r="5"/>
      <circle cx="371" cy="2432" r="5"/><circle cx="677" cy="2432" r="5"/><circle cx="983" cy="2432" r="5"/>
    </g>
    <path d="M141.5 2300 A76.5 76.5 0 0 1 294.5 2300 A76.5 76.5 0 0 0 447.5 2300 A76.5 76.5 0 0 1 600.5 2300 A76.5 76.5 0 0 0 753.5 2300 A76.5 76.5 0 0 1 906.5 2300 A76.5 76.5 0 0 0 1059.5 2300" stroke="url(#wave)" stroke-width="24"/>
    <g fill="#fbf6f0" filter="url(#soft)">
      <circle cx="218" cy="2300" r="60"/><circle cx="371" cy="2300" r="60"/><circle cx="524" cy="2300" r="60"/>
      <circle cx="677" cy="2300" r="60"/><circle cx="830" cy="2300" r="60"/><circle cx="983" cy="2300" r="60"/>
    </g>
    <g stroke="#b97650" stroke-width="2" fill="none" stroke-linecap="round">
      <circle cx="223" cy="2292" r="12"/><circle cx="223" cy="2292" r="5"/><path d="M200 2318c-4-14 0-26 10-32M205 2318h14"/>
      <circle cx="371" cy="2300" r="20"/><path d="M371 2282v36M371 2300l-10-8M371 2308l10-8M355 2306h32"/>
      <circle cx="521" cy="2297" r="15"/><circle cx="521" cy="2297" r="6"/><path d="M532 2308l12 12M506 2322v-10M514 2322v-6"/>
      <rect x="664" y="2278" width="24" height="34" rx="2"/><path d="M670 2288h12M670 2295h12M670 2302h7"/><circle cx="686" cy="2310" r="8"/><path d="M682 2310l3 3 5-6"/>
      <path d="M810 2300a20 20 0 0 1 34-14M850 2300a20 20 0 0 1-34 14M844 2280v6h-6M816 2320v-6h6"/><circle cx="830" cy="2300" r="8"/>
      <path d="M965 2296l18-9 18 9v20l-18 9-18-9zM965 2296l18 9 18-9M983 2305v20"/><circle cx="983" cy="2285" r="7"/><path d="M979 2285l3 3 5-5"/>
    </g>
  </svg>
</section>

<section class="storage">
  <h2 class="abs section-title" style="top:2665px">STORAGE &amp; LOGISTICS</h2>
  <p class="abs lead" style="top:2759px">We provide integrated storage solutions to support product stability and supply<br>chain continuity.</p>

  <div class="abs store-card" style="left:112px">
    <svg width="104" height="104" viewBox="0 0 104 104"><defs><linearGradient id="dg" x1="0" y1="0" x2="1" y2="1"><stop offset="0" stop-color="#c9875b"/><stop offset="1" stop-color="#9d5e3b"/></linearGradient></defs>
      <rect x="22" y="22" width="60" height="60" rx="12" transform="rotate(45 52 52)" fill="url(#dg)"/>
      <g stroke="#fff" stroke-width="1.8" fill="none"><path d="M36 46l16-10 16 10v20H36z"/><rect x="42" y="50" width="20" height="16"/><path d="M52 52v12M46 58h12"/></g>
    </svg>
    <h3>Cold Chain<br>Storage</h3><div class="dot"></div>
    <p>Temperature-controlled environments for sensitive products</p>
  </div>
  <div class="abs store-card" style="left:449px">
    <svg width="104" height="104" viewBox="0 0 104 104">
      <rect x="22" y="22" width="60" height="60" rx="12" transform="rotate(45 52 52)" fill="url(#dg)"/>
      <g stroke="#fff" stroke-width="1.8" fill="none"><path d="M36 38v30M68 38v30M36 52h32M36 66h32"/><rect x="42" y="42" width="8" height="10"/><rect x="53" y="56" width="10" height="10"/></g>
    </svg>
    <h3>Warehouse<br>Storage</h3><div class="dot"></div>
    <p>Scalable dry storage for finished goods and raw materials</p>
  </div>
  <div class="abs store-card" style="left:786px">
    <svg width="104" height="104" viewBox="0 0 104 104">
      <rect x="22" y="22" width="60" height="60" rx="12" transform="rotate(45 52 52)" fill="url(#dg)"/>
      <g stroke="#fff" stroke-width="1.8" fill="none"><path d="M36 52a16 16 0 0 1 28-11M68 52a16 16 0 0 1-28 11M64 36v6h-6M40 68v-6h6"/><circle cx="52" cy="52" r="6"/></g>
    </svg>
    <h3>Controlled<br>Atmosphere Storage</h3><div class="dot"></div>
    <p>Optimized conditions to maintain product quality and extend shelf life</p>
  </div>

  <p class="abs lead" style="top:3294px">Integrated with production, our storage capabilities allow for seamless transition<br>from processing to packaging and distribution.</p>
</section>

<section>
  <div class="abs cta" role="img" aria-label="Warm copper-toned view of a food processing facility"></div>
  <h2 class="abs cta-title">LET’S BUILD SOMETHING<br>TOGETHER</h2>
  <p class="abs cta-text">Tell us about your product, your category, and your timeline. We’ll take it from<br>concept to shelf.</p>
  <a class="abs btn btn-cta">Start a Project</a>
</section>

<footer class="site-footer">
  <div class="abs logo">Tarquel</div>
  <nav class="abs foot-nav">
    <span>Home</span><span>About</span><span>Applications</span><span>Capabilities</span><span>Quality &amp; Traceability</span><span>Why Tarquel</span><span>Contact</span>
  </nav>
  <div class="abs foot-rule"></div>
  <p class="abs copyright">© 2026 ALL RIGHTS RESERVED</p>
  <span class="abs social primary" style="left:965px" aria-label="Social link"></span>
  <span class="abs social" style="left:1007px" aria-label="Social link"></span>
  <span class="abs social" style="left:1050px" aria-label="Social link"></span>
</footer>

</body>
</html>
```